Redesign of business card for Birchline Mechanical

We are looking for a new design for our business cards for Birchline Mechanical. We are a plumbing & HVAC construction company, operating on the West Coast of Canada and USA. Logo attached.
Industry/Entity Type
Construction - Plumbing & HVAC
Contact Information for Business Card
Name, address, phone numbers, email, website address
Look and feel
Each slider illustrates characteristics of the customer's brand and the style your logo design should communicate.

```html
<!DOCTYPE html>
<html lang="en">
<head>
<meta charset="utf-8">
<title>Birchline Mechanical — Business Card</title>
<link href="https://fonts.googleapis.com/css2?family=Inter:wght@400;500;600&family=Mrs+Saint+Delafield&display=swap" rel="stylesheet">
<style>
  :root {
    --canvas: #979797;
    --slate: #4a5161;
    --slate-mark: #5a6273;
    --tagline: #a3a8b4;
    --paper: #ffffff;
    --ink: #4a5161;
    --muted: #a2a6af;
    --rule: #c9ccd2;
  }
  html, body {
    margin: 0;
    padding: 0;
    width: 1200px;
    height: 1000px;
    overflow: hidden;
    background: var(--canvas);
    font-family: "Inter", Arial, sans-serif;
  }
  .canvas { position: relative; width: 1200px; height: 1000px; }
  .card {
    position: absolute;
    left: 293px;
    width: 615px;
    height: 353px;
    border-radius: 20px;
    box-shadow: 6px 8px 14px rgba(0,0,0,0.28);
    overflow: hidden;
  }
  .card--front { top: 90px; background: var(--slate); }
  .card--back { top: 512px; background: var(--paper); }

  .front__name {
    position: absolute;
    left: 0; right: 0;
    top: 232px;
    text-align: center;
    font-weight: 600;
    font-size: 34px;
    letter-spacing: 3px;
    color: var(--slate-mark);
    text-transform: uppercase;
  }
  .front__tagline {
    position: absolute;
    left: 0; right: 0;
    top: 284px;
    text-align: center;
    font-family: "Mrs Saint Delafield", cursive;
    font-size: 34px;
    color: var(--tagline);
  }

  .brand {
    position: absolute;
    left: 57px;
    top: 152px;
    display: flex;
    align-items: center;
    gap: 12px;
  }
  .brand__square { width: 14px; height: 14px; background: var(--ink); }
  .brand__name {
    font-weight: 500;
    font-size: 16px;
    line-height: 18px;
    letter-spacing: 1.2px;
    color: var(--ink);
    text-transform: uppercase;
  }
  .divider {
    position: absolute;
    left: 307px;
    top: 97px;
    width: 1px;
    height: 159px;
    background: var(--rule);
  }
  .contact {
    position: absolute;
    left: 337px;
    top: 96px;
  }
  .contact__name { font-weight: 600; font-size: 17px; color: var(--ink); line-height: 21px; }
  .contact__role { font-weight: 500; font-size: 15px; color: var(--ink); line-height: 20px; }
  .contact__address {
    margin-top: 7px;
    font-size: 14px;
    line-height: 17px;
    color: var(--muted);
  }
  .contact__list { list-style: none; margin: 8px 0 0; padding: 0; }
  .contact__item {
    display: flex;
    align-items: center;
    gap: 12px;
    font-size: 14px;
    line-height: 17px;
    color: var(--muted);
  }
  .contact__icon { width: 11px; height: 11px; fill: var(--ink); flex: none; }
</style>
</head>
<body>
<main class="canvas">
  <section class="card card--front" aria-label="Card front">
    <div class="front__name">Birchline</div>
    <div class="front__tagline">Let's build something together</div>
  </section>

  <section class="card card--back" aria-label="Card back">
    <div class="brand">
      <span class="brand__square"></span>
      <div class="brand__name">Birchline<br>Mechanical</div>
    </div>
    <div class="divider"></div>
    <div class="contact">
      <div class="contact__name">Name Surname</div>
      <div class="contact__role">Position</div>
      <div class="contact__address">4120 Harbor Lane<br>Suite 200, Irvine<br>CA 92614</div>
      <ul class="contact__list">
        <li class="contact__item">
          <svg class="contact__icon" viewBox="0 0 24 24"><path d="M6.6 10.8a15.1 15.1 0 0 0 6.6 6.6l2.2-2.2c.3-.3.7-.4 1-.2 1.1.4 2.3.6 3.6.6.6 0 1 .4 1 1V20c0 .6-.4 1-1 1C10.6 21 3 13.4 3 4c0-.6.4-1 1-1h3.5c.6 0 1 .4 1 1 0 1.3.2 2.5.6 3.6.1.3 0 .7-.2 1z"/></svg>
          555-014-2290
        </li>
        <li class="contact__item">
          <svg class="contact__icon" viewBox="0 0 24 24"><path d="M2 5h20v14H2z M3 6l9 7 9-7" fill="var(--ink)"/><path d="M3 6.5l9 7 9-7" fill="none" stroke="#fff" stroke-width="1.6"/></svg>
          info@birchlinemech.com
        </li>
        <li class="contact__item">
          <svg class="contact__icon" viewBox="0 0 24 24"><circle cx="12" cy="12" r="10"/><path d="M2 12h20M12 2c3 3 3 17 0 20M12 2c-3 3-3 17 0 20M4 7h16M4 17h16" fill="none" stroke="#fff" stroke-width="1.3"/></svg>
          birchlinemech.com
        </li>
      </ul>
    </div>
  </section>
</main>
</body>
</html>
```